continued... Web Design for Professional Development and marketplace

in addition to the homepages that you are desiging, can you also create designs for the attached wireframes that are part of the same website.
I am creating this as a seperate project as we are keen to see your designs for the rest of the website.
VIdeo of prototype and homepage designs
https://www.filquarry.net/sh/qm7rtp2vbx9kka3/J2wNo8LpXe/design
Updates
added an additional wireframe that was missed in the original upload
added one more wireframe for the homepage: where the user is prompted to login or signup
Industry/Entity Type
Marketplace
Look and feel
Each slider illustrates characteristics of the customer's brand and the style your logo design should communicate.

```html
<!DOCTYPE html>
<html lang="en">
<head>
<meta charset="utf-8">
<title>Harwick School of Business — Provider Plans</title>
<link href="https://fonts.googleapis.com/css2?family=Open+Sans:wght@300;400;600;700&display=swap" rel="stylesheet">
<style>
  :root {
    --ink-dark: #2c333d;
    --slate: #4e5865;
    --orange: #f29c12;
    --orange-deep: #e08a0e;
    --blue: #3d8ac4;
    --text: #444a52;
    --muted: #5c636b;
    --rule: #d6d8db;
    --white: #ffffff;
    --chip: #eceef0;
  }
  * { box-sizing: border-box; margin: 0; padding: 0; }
  html, body { width: 891px; height: 1200px; overflow: hidden; background: var(--white); }
  body { position: relative; font-family: 'Open Sans', Arial, sans-serif; color: var(--text); }

  .site-header { position: absolute; top: 0; left: 0; width: 891px; height: 60px; background: var(--ink-dark); }
  .menu-btn { position: absolute; left: 81px; top: 11px; width: 44px; height: 35px; background: var(--slate); border-radius: 2px; }
  .search { position: absolute; left: 126px; top: 11px; width: 121px; height: 35px; background: var(--white); font-size: 12px; color: #a0a4a8; padding: 10px 9px; }
  .search-btn { position: absolute; left: 247px; top: 11px; width: 37px; height: 35px; background: var(--slate); }
  .brand { position: absolute; left: 340px; top: 7px; width: 212px; text-align: center; color: var(--white); line-height: 1; }
  .brand-name { font-size: 23px; font-weight: 400; display: block; }
  .brand-sub { font-size: 15px; font-weight: 300; display: block; margin-top: 3px; }
  .signup { position: absolute; left: 553px; top: 24px; font-size: 10px; color: var(--white); font-weight: 600; }
  .signup span { color: #8a9099; font-weight: 400; }
  .login-btn { position: absolute; left: 613px; top: 11px; width: 78px; height: 35px; background: var(--slate); border-radius: 2px; color: var(--white); font-size: 12px; font-weight: 600; display: flex; align-items: center; justify-content: center; gap: 6px; }
  .review-btn { position: absolute; left: 693px; top: 11px; width: 116px; height: 35px; background: var(--orange); border-radius: 2px; color: var(--white); font-size: 12px; font-weight: 600; display: flex; align-items: center; justify-content: center; gap: 6px; }

  .sub-nav { position: absolute; top: 60px; left: 0; width: 891px; height: 24px; background: var(--orange); display: flex; justify-content: flex-end; gap: 21px; padding-right: 82px; align-items: center; font-size: 10px; color: var(--white); }

  .filters { position: absolute; top: 89px; left: 81px; width: 728px; height: 52px; display: flex; border: 1px solid var(--rule); }
  .filter { flex: 1; border-left: 1px solid var(--rule); text-align: center; font-size: 11px; color: var(--muted); padding-top: 9px; line-height: 1.2; }
  .filter i { display: block; width: 9px; height: 8px; margin: 0 auto 2px; background: #b9bdc2; border-radius: 2px; }
  .filter small { display: block; color: var(--orange-deep); font-size: 9px; margin-top: 1px; }
  .filter.save { flex: 0 0 75px; background: var(--orange); color: var(--white); font-weight: 700; border-left: 0; padding-top: 13px; }
  .filter.save i { background: var(--white); }
  .filter.wide { flex: 1.4; }

  .page-title { position: absolute; left: 80px; top: 162px; font-size: 24px; font-weight: 700; color: var(--orange-deep); }
  .page-sub { position: absolute; left: 80px; top: 193px; font-size: 12px; color: var(--text); }
  .title-rule { position: absolute; left: 81px; top: 219px; width: 728px; height: 1px; background: var(--rule); }

  .plan { position: absolute; top: 262px; width: 224px; height: 219px; border: 1px solid #e2e4e6; box-shadow: 0 1px 2px rgba(0,0,0,.08); text-align: center; }
  .plan-head { height: 45px; color: var(--white); padding-top: 6px; line-height: 1.1; }
  .plan-head b { display: block; font-size: 16px; font-weight: 700; }
  .plan-head span { display: block; font-size: 12.5px; font-weight: 700; margin-top: 1px; }
  .plan-body { padding: 17px 6px 0; font-size: 11.5px; font-weight: 300; line-height: 18px; color: var(--muted); }
  .plan-body p + p { margin-top: 6px; }
  .plan-body p.gap { margin-top: 27px; }
  .basic { left: 82px; } .basic .plan-head { background: var(--orange); }
  .standard { left: 333px; } .standard .plan-head { background: var(--blue); }
  .advanced { left: 584px; } .advanced .plan-head { background: var(--slate); }

  .trial-btn { position: absolute; left: 334px; top: 521px; width: 222px; height: 46px; background: var(--orange); color: var(--white); text-align: center; padding-top: 9px; line-height: 1.3; }
  .trial-btn b { display: block; font-size: 11.5px; font-weight: 600; }
  .trial-btn span { display: block; font-size: 9.5px; margin-top: 2px; }

  .photo { position: absolute; width: 287px; height: 222px; }
  .photo-laptop { left: 82px; top: 648px; background: linear-gradient(135deg, #f4ede2 0%, #e9e2d8 55%, #d8d6d4 100%); }
  .photo-notes { left: 524px; top: 932px; background: linear-gradient(120deg, #5d6f8a 0%, #c9cdd4 40%, #f1f2f3 100%); }

  .feature { position: absolute; width: 389px; font-size: 12px; font-weight: 300; line-height: 18px; color: var(--muted); }
  .feature h2 { font-size: 17px; font-weight: 400; color: var(--text); margin-bottom: 29px; line-height: 1.2; }
  .feature p { margin-bottom: 18px; text-align: justify; }
  .manage { left: 420px; top: 644px; }
  .reporting { left: 83px; top: 927px; }
</style>
</head>
<body>
  <header class="site-header">
    <div class="menu-btn">
      <svg width="44" height="35" viewBox="0 0 44 35"><g fill="#fff"><rect x="9" y="9" width="26" height="3"/><rect x="9" y="16" width="26" height="3"/><rect x="9" y="23" width="26" height="3"/></g></svg>
    </div>
    <div class="search">Search</div>
    <div class="search-btn">
      <svg width="37" height="35" viewBox="0 0 37 35"><circle cx="17" cy="16" r="5" fill="none" stroke="#fff" stroke-width="2.2"/><line x1="20.5" y1="19.5" x2="25" y2="24" stroke="#fff" stroke-width="2.6"/></svg>
    </div>
    <div class="brand"><span class="brand-name">Harwick School</span><span class="brand-sub">of Business</span></div>
    <div class="signup">Sign Up <span>or</span></div>
    <div class="login-btn">
      <svg width="14" height="15" viewBox="0 0 14 15"><circle cx="7" cy="4" r="3.5" fill="#fff"/><path d="M0 15c0-5 3-7 7-7s7 2 7 7z" fill="#fff"/></svg>Login
    </div>
    <div class="review-btn">
      <svg width="20" height="15" viewBox="0 0 20 15"><rect x="1" y="1" width="15" height="11" fill="none" stroke="#fff" stroke-width="1.3"/><line x1="4" y1="5" x2="13" y2="5" stroke="#fff"/><line x1="4" y1="8" x2="11" y2="8" stroke="#fff"/><circle cx="16" cy="11" r="3.5" fill="#fff"/></svg>Add Review
    </div>
  </header>

  <nav class="sub-nav">
    <span>About</span><span>Business</span><span>Developers</span><span>Pricacy &amp; Terms</span><span>Copyright &amp; Trademark</span>
  </nav>

  <div class="filters">
    <div class="filter save"><i></i>Save</div>
    <div class="filter"><i></i>Career<small>(all)</small></div>
    <div class="filter wide"><i></i>Specialization<small>(all)</small></div>
    <div class="filter wide"><i></i>Location<small>(Vancouver)</small></div>
    <div class="filter wide"><i></i>Price<small>($600-$3000)</small></div>
    <div class="filter wide"><i></i>Start Date<small>(2-6 months)</small></div>
    <div class="filter wide"><i></i>Level<small>(intermediate)</small></div>
    <div class="filter"><i></i>Type<small>(multiple)</small></div>
    <div class="filter"><i></i>Provider<small>(one)</small></div>
  </div>

  <h1 class="page-title">Lorem ipsum dolor sit amet</h1>
  <p class="page-sub">Vestibulum sit amet orci vitae nulla</p>
  <div class="title-rule"></div>

  <section class="plan basic">
    <div class="plan-head"><b>BASIC</b><span>$100 per month</span></div>
    <div class="plan-body"><p>Manage dates and locations for<br>upcoming sessions</p></div>
  </section>
  <section class="plan standard">
    <div class="plan-head"><b>STANDARD</b><span>$200 per month</span></div>
    <div class="plan-body">
      <p>Manage dates and locations<br>for upcoming sessions for<br>up to 3 courses</p>
      <p class="gap">Analytics for your courses</p>
    </div>
  </section>
  <section class="plan advanced">
    <div class="plan-head"><b>ADVANCED</b><span>$500 per month</span></div>
    <div class="plan-body">
      <p>Manage dates and locations<br>for upcoming sessions for<br>UNLIMITED coursess</p>
      <p>Analytics for your courses and baseline<br>with comparable courses</p>
      <p>Add to New and Featured<br>for a month</p>
    </div>
  </section>

  <div class="trial-btn"><b>GET STARTED WITH A 60 DAY TRIAL</b><span>No obligation, no credit card required.</span></div>

  <div class="photo photo-laptop" role="img" aria-label="Photo of a woman lying on a bed working on a laptop"></div>
  <section class="feature manage">
    <h2>Manage your courses</h2>
    <p>If you are a provider of professional development, please sign-up for a chargeable provider account, so you you can manage the details of your courses. The community will still be providing the reviews and ratings.</p>
    <p>Find out how to easily synchronize your website updates with updates to this site. You will have access to anonymised data on which courses people are taking and track how many people sign-up for your course from this website.</p>
    <p>All user data is confidential and is not shared with anyone.</p>
  </section>

  <section class="feature reporting">
    <h2>Reporting</h2>
    <p>... view reports on your courses, similar courses and what is trending, to better attract more subscribers...</p>
    <p>Lorem ipsum dolor sit amet, consectetur adipiscing elit. Sed dolor arcu, pretium a rutrum et, volutpat at orci. Fusce purus magna, ullamcorper nec facilisis in, blandit vitae leo. Fusce sodales fringilla malesuada. Duis fringilla tincidunt felis et varius.</p>
    <p>Class aptent taciti sociosqu ad litora torquent per conubia nostra, per inceptos himenaeos. Integer iaculis lacus nisl, eget laoreet mi aliquet ut. Sed dignissim pulvinar mollis.</p>
  </section>
  <div class="photo photo-notes" role="img" aria-label="Photo of a hand writing notes with a pen beside a laptop"></div>
</body>
</html>
```